Cans for flavored Macadamias

Brindle Creek Orchard Company (www.brindlecreekorchard.example) has been packaging 3 flavors of macadamia nuts in to 200g pouches for a number of years. We are about to change from 200g pouches to 80g cans. We need a fresh new look although the back ground colours must stay the same, Roasted & Salted = Yellow, Wasabi = Green, Abalone = Blue.
The can label and lid sticker will be printed 4 colour process. The trimmed finished sizes are, can label - L246 x H60mm and lid sticker 61mm diameter. The attached files show the existing front and back labels for the pouches. The health benefits, ingredients and nutrition facts information can used. Delete address and bar code but leave space for new ones. '80g Net' must show on the front of the can label. Product of Australia logo must be prominent on both can label and lid sticker.
The general feeling is we need to have a photo of a koala on there somewhere, maybe the lid. I have uploaded a photo that I hope you can use.
Updates

Target Market(s)

We're in all of Australia's duty free stores and a lot of souvenir stores. We do sell in to retails. Our target customers are primarily Asian hence the Wasabi and Abalone flavours.

Industry/Entity Type

It Company

Requirements
Must have
• If you google images for "buy Australian flavoured macadamias" it shows most of what's currently on the market. We obviously don't want to look the same as any of them.

```html
<!DOCTYPE html>
<html lang="en">
<head>
<meta charset="utf-8">
<title>Brindle Creek Macadamia Nuts – Lid Sticker and Can Label</title>
<link rel="stylesheet" href="https://fonts.googleapis.com/css2?family=Luckiest+Guy&family=Fredoka:wght@700&family=Chewy&family=Open+Sans:wght@400;600&display=swap">
<style>
  :root {
    --bg: #ffffff;
    --orange-light: #f5962a;
    --orange: #e8741a;
    --orange-deep: #cf5a0c;
    --cream: #f4efc4;
    --outline: #2b1a10;
    --red-brown: #b8300e;
    --flame-top: #f7c23a;
    --flame-bottom: #b2220c;
    --nut-light: #f4e6c8;
    --nut-mid: #dcc09a;
    --badge-green: #1e7a3a;
  }
  * { margin: 0; padding: 0; box-sizing: border-box; }
  html, body {
    width: 1200px; height: 923px; overflow: hidden;
    background: var(--bg);
  }
  .artboard { position: relative; width: 1200px; height: 923px; }
  .artboard svg { position: absolute; left: 0; top: 0; }
  .title-macadamia {
    font-family: "Luckiest Guy", "Arial Black", Impact, sans-serif;
    fill: url(#flame);
    stroke: var(--outline);
    stroke-width: 2;
    paint-order: stroke;
  }
  .title-nuts {
    font-family: "Fredoka", "Arial Rounded MT Bold", sans-serif;
    font-weight: 700;
    fill: var(--cream);
    stroke: var(--outline);
    stroke-width: 5;
    paint-order: stroke;
  }
  .flavour {
    font-family: "Chewy", "Arial Black", sans-serif;
    fill: var(--red-brown);
    stroke: #5a1505;
    stroke-width: 1.5;
    paint-order: stroke;
  }
  .net-weight {
    font-family: "Open Sans", sans-serif;
    font-weight: 400;
    fill: var(--cream);
  }
  .company-name {
    font-family: "Open Sans", sans-serif;
    fill: var(--cream);
  }
</style>
</head>
<body>
<main class="artboard">
  <svg width="1200" height="923" viewBox="0 0 1200 923" xmlns="http://www.w3.org/2000/svg">
    <defs>
      <radialGradient id="sticker-fill" cx="50%" cy="45%" r="55%">
        <stop offset="0" stop-color="var(--orange-light)"/>
        <stop offset="0.7" stop-color="var(--orange)"/>
        <stop offset="1" stop-color="var(--orange-deep)"/>
      </radialGradient>
      <linearGradient id="label-fill" x1="0" y1="0" x2="1" y2="0">
        <stop offset="0" stop-color="var(--orange-deep)"/>
        <stop offset="0.45" stop-color="var(--orange-light)"/>
        <stop offset="1" stop-color="var(--orange-deep)"/>
      </linearGradient>
      <linearGradient id="flame" x1="0" y1="0" x2="0" y2="1">
        <stop offset="0" stop-color="var(--flame-top)"/>
        <stop offset="1" stop-color="var(--flame-bottom)"/>
      </linearGradient>
      <radialGradient id="nuts-fill" cx="50%" cy="50%" r="60%">
        <stop offset="0" stop-color="var(--nut-light)"/>
        <stop offset="0.6" stop-color="var(--nut-mid)" stop-opacity="0.85"/>
        <stop offset="1" stop-color="var(--orange)" stop-opacity="0"/>
      </radialGradient>
      <path id="sticker-top-arc" d="M 168 480 A 162 162 0 0 1 492 480"/>
      <path id="sticker-bottom-arc" d="M 150 470 A 180 180 0 0 0 510 470"/>
      <path id="label-flavour-arc" d="M 660 590 Q 830 670 1000 590"/>
    </defs>

    <!-- Lid sticker -->
    <g class="lid-sticker">
      <circle cx="330" cy="480" r="210" fill="url(#sticker-fill)"/>
      <text class="title-macadamia" font-size="52" text-anchor="middle" textLength="420" lengthAdjust="spacingAndGlyphs">
        <textPath href="#sticker-top-arc" startOffset="50%" textLength="420" lengthAdjust="spacingAndGlyphs">MACADAMIA</textPath>
      </text>
      <text class="company-name" font-size="13" text-anchor="middle">
        <tspan x="330" y="390">Brindle Creek</tspan>
        <tspan x="330" y="408">Orchard</tspan>
        <tspan x="330" y="426">Company</tspan>
      </text>
      <text class="title-nuts" x="330" y="520" font-size="92" text-anchor="middle" textLength="230" lengthAdjust="spacingAndGlyphs">NUTS</text>
      <text class="net-weight" x="330" y="588" font-size="38" text-anchor="middle">80g Net</text>
      <text class="flavour" font-size="30" text-anchor="middle">
        <textPath href="#sticker-bottom-arc" startOffset="50%" textLength="400" lengthAdjust="spacingAndGlyphs">ROASTED AND SALTED</textPath>
      </text>
    </g>

    <!-- Can label front panel -->
    <g class="can-label">
      <rect x="630" y="150" width="395" height="660" rx="6" fill="url(#label-fill)"/>
      <g role="img" aria-label="Photograph of roasted macadamia nuts">
        <rect x="640" y="330" width="380" height="330" rx="40" fill="url(#nuts-fill)"/>
      </g>
      <text class="title-macadamia" x="827" y="330" font-size="60" text-anchor="middle" textLength="345" lengthAdjust="spacingAndGlyphs">MACADAMIA</text>
      <text class="title-nuts" x="827" y="530" font-size="150" text-anchor="middle" textLength="350" lengthAdjust="spacingAndGlyphs">NUTS</text>
      <text class="flavour" font-size="32" text-anchor="middle">
        <textPath href="#label-flavour-arc" startOffset="50%" textLength="330" lengthAdjust="spacingAndGlyphs">ROASTED AND SALTED</textPath>
      </text>
      <circle class="origin-badge" cx="680" cy="728" r="36" fill="var(--badge-green)" aria-label="Place for Product of Australia badge"/>
      <text class="net-weight" x="820" y="760" font-size="40" text-anchor="middle">80g Net</text>
      <text class="company-name" font-size="20" text-anchor="end">
        <tspan x="1012" y="705">Brindle Creek</tspan>
        <tspan x="1012" y="733">Orchard</tspan>
        <tspan x="1012" y="761">Company</tspan>
      </text>
    </g>
  </svg>
</main>
</body>
</html>
```